Stationery Refresh For Local Mortgage Broker

We want to modernise and standardise our stationery, including: letterhead, presentation folder, email signature and business card.

The new stationery should be a more modern and professional take on our existing colour scheme and brand. (We do not want a complete overhaul.) A folder of approved stock photos can be found here: https://filebox.example-share.net/f/7kQzR2mTn4vWx9Lp3Yb8-HsdJe5Uc1Ga/view

Our current website is: www.brindlecovefin.com.au but we will be updating this to be consistent with our new stationery.

We are open to *very slight* tweaks to our logo if you feel it needs modernising, but overall we would like to maintain consistent colour scheme.

> Letterhead

148 Calloway Parade,
Geelong, VIC, 3220
ABN: 31 805 249 067
Australian Credit License: 718293

(03) 5391 6084
www.brindlecovefin.com.au

> Presentation Folder

148 Calloway Parade,
Geelong, VIC, 3220
(03) 5391 6084
www.brindlecovefin.com.au

ABN: 31 805 249 067

> Email Signature

Liam Tresidder
Director
M. 0412 857 294
P. (03) 5391 6084
www.brindlecovefin.com.au
148 Calloway Parade,
Geelong, VIC, 3220

ABN: 31 805 249 067

(you can also include a photo if you like: https://brindlecovefin.com.au/wp-content/uploads/2020/12/Liam-Tresidder.png.webp)

> Business Card

Liam Tresidder
Director
M. 0412 857 294
P. (03) 5391 6084
www.brindlecovefin.com.au
148 Calloway Parade,
Geelong, VIC, 3220

ABN: 31 805 249 067

Additional information...

If it's useful/relevant, the services we offer are: Home Loans, Investment Loans, Refinance, Debt Consolidation, Commercial Finance, Vehicle Loans
(You may choose to use this in any of the designs)

Target Market(s)

Home Buyers and Investors

Industry/Entity Type

Mortgage broking/property/real estate

Requirements
Must have
• At least somewhat consistent with our current site (yet meaningfully modernized)
Should not have
• dramatically different logo or colourscheme overhauls

```html
<!DOCTYPE html>
<html lang="en">
<head>
<meta charset="utf-8">
<title>Brindle Cove Finance — Business Card</title>
<link href="https://fonts.googleapis.com/css2?family=Arimo:wght@400;700&display=swap" rel="stylesheet">
<style>
  :root {
    --brand-red: #a4121a;
    --ink-grey: #5a5a5a;
    --rule-grey: #8a8a8a;
    --card-white: #fbfbfa;
    --backdrop: #e4e4e2;
  }
  * { box-sizing: border-box; margin: 0; padding: 0; }
  html, body {
    width: 1200px; height: 801px; overflow: hidden;
    background: var(--backdrop);
    font-family: "Arimo", Arial, sans-serif;
  }
  .sheet {
    width: 1200px; height: 801px;
    display: flex; align-items: center; justify-content: center; gap: 40px;
  }
  .card {
    width: 560px; height: 320px;
    background: var(--card-white);
    border-bottom: 4px solid var(--brand-red);
    box-shadow: 0 10px 24px rgba(0,0,0,0.12);
    position: relative;
    display: flex; flex-direction: column; align-items: center;
  }
  .wordmark {
    display: flex; flex-direction: column; align-items: center;
    color: var(--brand-red); font-weight: 400; text-transform: uppercase;
  }
  .wordmark__name { font-size: 34px; letter-spacing: 0.42em; margin-right: -0.42em; }
  .wordmark__sub { font-size: 13px; letter-spacing: 0.62em; margin-right: -0.62em; margin-top: 8px; }

  /* front */
  .card--front .wordmark { margin-top: 44px; }
  .contact {
    display: flex; margin-top: 34px; width: 100%; justify-content: center;
  }
  .contact__person { text-align: right; padding-right: 20px; width: 250px; }
  .contact__rule { width: 1px; background: var(--rule-grey); height: 118px; }
  .contact__details { padding-left: 20px; width: 250px; color: var(--ink-grey); font-size: 13px; line-height: 1.45; }
  .person__name { color: var(--brand-red); font-weight: 700; font-size: 20px; }
  .person__role { color: var(--ink-grey); font-size: 15px; margin-top: 2px; }
  .person__reg { color: var(--ink-grey); font-size: 12.5px; margin-top: 22px; line-height: 1.4; }
  .person__reg b { font-weight: 700; }
  .detail-line { display: flex; align-items: center; gap: 7px; }
  .detail-line svg { width: 11px; height: 11px; flex: none; }
  .address { margin-bottom: 6px; }
  .web { color: var(--ink-grey); }
  .web span { color: var(--brand-red); }

  /* back */
  .card--back { justify-content: center; }
  .services {
    margin-top: 34px; color: var(--ink-grey); font-size: 15px; line-height: 1.7;
    text-align: center;
  }
  .services li { display: inline; list-style: none; }
  .services li::before { content: "\25CF"; color: var(--brand-red); font-size: 11px; margin: 0 5px 0 8px; vertical-align: 1px; }
</style>
</head>
<body>
<main class="sheet">
  <section class="card card--front">
    <div class="wordmark">
      <span class="wordmark__name">Brindle Cove</span>
      <span class="wordmark__sub">Finance</span>
    </div>
    <div class="contact">
      <div class="contact__person">
        <p class="person__name">Liam Tresidder</p>
        <p class="person__role">Director</p>
        <p class="person__reg"><b>ABN:</b> 31 805 249 067<br><b>Australian Credit License:</b> 718293</p>
      </div>
      <div class="contact__rule"></div>
      <div class="contact__details">
        <p class="address">148 Calloway Parade,<br>Geelong, VIC, 3220</p>
        <p class="detail-line">
          <svg viewBox="0 0 12 12" aria-hidden="true"><path fill="#a4121a" d="M2.5 1l2 2.2-1.1 1.3a7 7 0 0 0 4.1 4.1l1.3-1.1L11 9.5 9.8 11C5 10.6 1.4 7 1 2.2z"/></svg>
          (03) 5391 6084</p>
        <p class="detail-line">
          <svg viewBox="0 0 12 12" aria-hidden="true"><rect x="3" y="0.8" width="6" height="10.4" rx="1" fill="none" stroke="#a4121a" stroke-width="1.2"/><circle cx="6" cy="9.4" r="0.6" fill="#a4121a"/></svg>
          0412 857 294</p>
        <p class="detail-line web">
          <svg viewBox="0 0 12 12" aria-hidden="true"><circle cx="6" cy="6" r="5" fill="none" stroke="#a4121a" stroke-width="1.2"/><path d="M1 6h10M6 1c-2.5 3-2.5 7 0 10M6 1c2.5 3 2.5 7 0 10" fill="none" stroke="#a4121a" stroke-width="1"/></svg>
          www.<span>brindlecovefin.com.au</span></p>
      </div>
    </div>
  </section>

  <section class="card card--back">
    <div class="wordmark">
      <span class="wordmark__name">Brindle Cove</span>
      <span class="wordmark__sub">Finance</span>
    </div>
    <ul class="services">
      <li>Home Loans</li><li>Investment Loans</li><li>Refinance</li><br>
      <li>Debt Consolidation</li><li>Commercial Finance</li><li>Vehicle Loans</li>
    </ul>
  </section>
</main>
</body>
</html>
```